I need creative and unique business card design using my company logo. Ok to change logo color. We are a small brokerage doing both Real Estate and Mortgage services. Need to have the follow on business card;
1. agent name - Nora Velden - Realtor
2. cell - 949-555-0182
3. license number - DRE 07164392
4. business name - Bright Keys & Lending, Inc
5. business office - 626-555-0147
6. business address - 214 W. Marlowe Ave #308, Arcadia CA 91006
7. business logo - attached (ok to use different color on logo)

```html
<!DOCTYPE html>
<html lang="en">
<head>
<meta charset="utf-8">
<title>Bright Keys &amp; Lending – Business Card</title>
<link rel="stylesheet" href="https://fonts.googleapis.com/css2?family=Montserrat:wght@400;500;700&display=swap">
<style>
  :root {
    --backdrop: #2e2f31;
    --card-white: #ffffff;
    --card-black: #1c1c1d;
    --brand-blue: #2f7fd0;
    --brand-deep: #1f4fa8;
    --brand-light: #5aaee3;
    --ink: #1a1a1a;
    --silver: #b9bbbe;
  }
  html, body {
    margin: 0;
    width: 1200px;
    height: 1200px;
    overflow: hidden;
    background: var(--backdrop);
    font-family: "Montserrat", sans-serif;
  }
  .canvas {
    position: relative;
    width: 1200px;
    height: 1200px;
  }
  .card {
    position: absolute;
    left: 250px;
    width: 700px;
    height: 400px;
    border-radius: 26px;
    overflow: hidden;
    box-sizing: border-box;
  }
  .card-front {
    top: 140px;
    background: var(--card-white);
    border-bottom: 4px solid var(--brand-blue);
  }
  .card-back {
    top: 660px;
    background: var(--card-black);
    border-bottom: 4px solid var(--brand-blue);
  }
  .front-band {
    position: absolute;
    left: 0;
    bottom: 0;
    width: 460px;
    height: 34px;
    background: linear-gradient(90deg, var(--brand-light), var(--brand-deep));
    clip-path: polygon(0 70%, 90% 0, 100% 0, 100% 100%, 0 100%);
  }
  .agent {
    position: absolute;
    left: 60px;
    top: 120px;
  }
  .agent-name {
    margin: 0;
    font-size: 40px;
    font-weight: 700;
    color: var(--brand-blue);
    letter-spacing: 1px;
    line-height: 1;
  }
  .agent-title {
    margin: 4px 0 18px;
    font-size: 20px;
    font-weight: 500;
    color: var(--ink);
    letter-spacing: 1px;
  }
  .contact {
    list-style: none;
    margin: 0;
    padding: 0;
    font-size: 18px;
    color: var(--ink);
    line-height: 1.35;
  }
  .contact li {
    display: flex;
    align-items: flex-start;
    gap: 12px;
  }
  .contact svg {
    width: 20px;
    height: 22px;
    flex: none;
    margin-top: 1px;
    fill: none;
    stroke: var(--brand-blue);
    stroke-width: 2;
  }
  .contact .icon-solid { fill: var(--brand-blue); stroke: none; }
  .license {
    margin: 12px 0 0 32px;
    font-size: 17px;
    color: var(--brand-blue);
  }
  .brand {
    position: absolute;
    display: flex;
    align-items: center;
    gap: 14px;
  }
  .brand-mark {
    width: 54px;
    height: 54px;
    flex: none;
  }
  .brand-name {
    font-weight: 700;
    line-height: 1.15;
  }
  .front-brand {
    right: 48px;
    top: 70px;
    width: 250px;
  }
  .front-brand .brand-mark { background: var(--brand-blue); }
  .front-brand .brand-name { color: var(--brand-blue); font-size: 22px; }
  .back-brand {
    left: 50%;
    top: 50%;
    transform: translate(-50%, -50%);
    flex-direction: column;
    gap: 22px;
    text-align: center;
  }
  .back-brand .brand-mark { width: 90px; height: 90px; background: var(--silver); }
  .back-brand .brand-name {
    color: var(--silver);
    font-size: 34px;
    letter-spacing: 4px;
    text-transform: uppercase;
  }
</style>
</head>
<body>
<main class="canvas">
  <section class="card card-front" aria-label="Card front">
    <div class="agent">
      <h1 class="agent-name">NORA VELDEN</h1>
      <p class="agent-title">REALTOR</p>
      <ul class="contact">
        <li>
          <svg viewBox="0 0 20 22" aria-hidden="true"><rect x="5" y="1" width="10" height="20" rx="2"/><line x1="9" y1="18" x2="11" y2="18"/></svg>
          <span>Cell 949-555-0182</span>
        </li>
        <li>
          <svg viewBox="0 0 20 22" aria-hidden="true"><path class="icon-solid" d="M4 2 L8 2 L9 7 L7 9 C8 12 10 14 13 15 L15 13 L19 14 L19 18 C19 19 18 20 17 20 C9 20 2 13 2 5 C2 3 3 2 4 2 Z"/></svg>
          <span>Office 626-555-0147</span>
        </li>
        <li>
          <svg viewBox="0 0 20 22" aria-hidden="true"><path d="M10 21 C10 21 3 13 3 8 A7 7 0 0 1 17 8 C17 13 10 21 10 21 Z"/><circle cx="10" cy="8" r="2.5"/></svg>
          <span>214 W. Marlowe Ave #308,<br>Arcadia CA 91006</span>
        </li>
      </ul>
      <p class="license">License number - DRE 07164392</p>
    </div>
    <div class="brand front-brand">
      <span class="brand-mark" aria-hidden="true"></span>
      <span class="brand-name">Bright Keys &amp; Lending, Inc</span>
    </div>
    <div class="front-band" aria-hidden="true"></div>
  </section>

  <section class="card card-back" aria-label="Card back">
    <div class="brand back-brand">
      <span class="brand-mark" aria-hidden="true"></span>
      <span class="brand-name">Bright Keys &amp; Lending, Inc</span>
    </div>
  </section>
</main>
</body>
</html>
```